KM Group

We need a new website for our company and since we had a very good work done for our logo in this site, we're back for the entire job.

Our company name is Halvorsen Capital Group. We're adding files of examples of what we have done today. In my opinion we need a more attention lock in the site but yet financial simple work.

Our files (attached) will let you know what we have so far. We need a complete change but the colours should be the same, however you can change them not running away to far from the original, and of course matching with the logo.

We need examples for 3 kind of layouts.

- A HOME welcome layout
- An internal Layout with sidebar
- And internal Layout wide

We can buy image licenses if needed for assets.
Actually there are 5 slide images placed on the Welcome HOME, we need those there, but you can improve with better images to match the new website!!!

Target Market(s)

Clients looking for financial advisers, tax and funds specialist, currency advisers

Industry/Entity Type

Financial

Requirements
Must have
• all the fonts must be in accordance with the financial market sites........the welcome home page must be precise, neat and information accurate........the menu should be elegant........main focus on the Home page, should be also the PRIVATE ACCESS box log in.......

```html
<!DOCTYPE html>
<html lang="en">
<head>
<meta charset="utf-8">
<title>Halvorsen Capital Group</title>
<link href="https://fonts.googleapis.com/css2?family=Roboto+Condensed:wght@400;700&family=Open+Sans:wght@400;600;700&display=swap" rel="stylesheet">
<style>
:root{
  --orange:#f47b20;
  --ink:#333;
  --text:#555;
  --page:#ebebeb;
  --band:#e3e3e3;
  --band2:#dadada;
  --nav:#f3f3f3;
  --foot:#b3b3b3;
  --foot2:#8f8f8f;
  --dark:#2f2f2f;
}
*{margin:0;padding:0;box-sizing:border-box}
html,body{width:971px;height:1200px;overflow:hidden}
body{position:relative;background:linear-gradient(#f0f0f0,#e6e6e6 400px);font-family:"Open Sans",Arial,sans-serif;color:var(--text)}
.abs{position:absolute}
.cond{font-family:"Roboto Condensed",Arial Narrow,sans-serif}

/* brand */
.brand{left:0;width:971px;top:40px;display:flex;justify-content:center;align-items:center;gap:10px}
.brand-mark{width:22px;height:22px;background:var(--orange)}
.brand-name{font-family:"Roboto Condensed",sans-serif;font-weight:700;font-size:26px;color:#222;letter-spacing:1px}

/* navigation */
.nav{left:71px;top:105px;width:829px;height:62px;background:var(--nav);display:flex}
.nav a{flex:1;display:flex;flex-direction:column;align-items:center;justify-content:center;font-size:9px;color:#333;text-decoration:none;letter-spacing:.3px;padding-top:2px}
.nav a.current{flex:0 0 97px;background:var(--orange);color:#fff}
.nav .caret{font-size:7px;line-height:7px;margin-top:2px;color:#666}

/* hero */
.hero-photo{left:405px;top:155px;width:476px;height:260px;background:radial-gradient(ellipse at 50% 60%,#5a5a5a,#9a9a9a 45%,rgba(220,220,220,0) 75%)}
.hero-title{left:119px;top:214px;font-family:"Roboto Condensed",sans-serif;font-weight:700;font-size:35px;color:var(--orange);line-height:40px}
.hero-sub{left:119px;top:250px;font-family:"Roboto Condensed",sans-serif;font-weight:700;font-size:20px;color:#444}
.hero-copy{left:119px;top:276px;width:270px;font-size:11px;line-height:15px;color:#222}
.hero-arrow{top:334px;width:19px;height:19px;border-radius:50%;background:var(--orange)}
.hero-arrow svg{display:block}

/* offer */
.offer{left:0;top:416px;width:971px;height:189px;background:var(--band);border-top:1px solid #d2d2d2}
.offer-title{left:88px;top:497px;font-family:"Roboto Condensed",sans-serif;font-weight:700;font-size:24px;color:var(--ink)}
.sep{top:440px;width:1px;height:136px;background:#c9c9c9}
.card{top:435px;width:158px}
.card .kicker{font-size:13px;color:var(--orange);line-height:16px}
.card h3{font-family:"Roboto Condensed",sans-serif;font-weight:700;font-size:24px;color:var(--ink);line-height:26px;margin-bottom:8px}
.card p{font-size:10.5px;line-height:13.5px;text-align:justify;color:#444;height:70px}
.btn{display:inline-block;margin-top:14px;width:77px;height:30px;background:var(--dark);color:#fff;font-size:10.5px;text-align:center;line-height:30px;border:1px solid #1e1e1e}

/* what we do */
.do{left:0;top:605px;width:971px;height:330px;background:var(--band2)}
.do-title{left:88px;top:624px;font-family:"Roboto Condensed",sans-serif;font-weight:700;font-size:24px;color:var(--ink)}
.do-copy{left:88px;top:661px;width:584px;font-size:10.5px;line-height:15.5px;text-align:justify;text-indent:22px;color:#666}
.do-more{left:617px;top:762px;font-size:11px;font-weight:700;color:#333}
.rates{left:88px;top:799px;width:584px;height:20px;background:#fafafa;border:1px solid #d0d0d0;display:flex;align-items:center;font-size:7.5px;font-weight:700}
.rates .label{width:74px;height:100%;background:#dedede;color:#555;font-size:10px;font-weight:400;display:flex;align-items:center;justify-content:center}
.rates span.pair{margin-left:9px;margin-right:12px;color:#2f6fb3}
.rates .down{color:#d21e1e}
.rates .up{color:#1e8a2e}

/* login */
.login{left:708px;top:624px;width:175px;height:200px;border-radius:5px;background:linear-gradient(#fff,#f1f1f1);border:1px solid #c8c8c8;box-shadow:0 1px 3px rgba(0,0,0,.15);overflow:hidden}
.login .forgot{position:absolute;right:12px;top:3px;font-size:5.5px;color:#555;text-decoration:underline}
.login .head{position:absolute;left:66px;top:14px;font-family:"Roboto Condensed",sans-serif;font-weight:700;font-size:20px;color:var(--orange)}
.login .key{position:absolute;left:26px;top:14px}
.login label{position:absolute;left:26px;font-size:6.5px;color:#444}
.login .field{position:absolute;left:26px;width:124px;height:20px;border:1px solid #aaa;border-radius:3px;background:linear-gradient(#d6d6d6,#eee);font-size:7px;color:#888;padding-left:10px;line-height:19px}
.login .remember{position:absolute;left:28px;top:144px;font-size:5.5px;color:#333;display:flex;align-items:center;gap:4px}
.login .bar{position:absolute;left:0;bottom:0;width:100%;height:38px;background:linear-gradient(#a9a9a9,#cfcfcf)}
.login .links{position:absolute;left:26px;top:9px;font-size:5.5px;line-height:10px;color:#fff}
.login .links b{color:#b0171c;font-weight:400;text-decoration:underline}
.login .go{position:absolute;right:22px;top:11px;width:46px;height:16px;border-radius:3px;background:linear-gradient(#4a4a4a,#1d1d1d);color:#fff;font-size:7px;font-weight:700;text-align:center;line-height:16px}

/* trust */
.rule{left:71px;top:843px;width:829px;height:1px;background:#a9a9a9}
.trust-label{left:116px;top:880px;font-size:11px;font-weight:700;color:#333}
.badge{top:870px}

/* footer */
.footer{left:0;top:935px;width:971px;height:150px;background:var(--foot)}
.fcol{top:955px;font-size:7px;line-height:10.8px;color:#555}
.fcol h4{font-size:8.5px;font-weight:600;color:var(--orange);margin-bottom:6px;line-height:11px}
.social{left:776px;top:956px;display:flex;gap:5px}
.social i{width:17px;height:17px;border-radius:50%;background:#8d8d8d;display:block}
.copy{left:684px;top:1057px;font-size:8px;color:#444}
.copy b{font-weight:600;color:#333}
.legal{left:0;top:1085px;width:971px;height:115px;background:var(--foot2)}
.legal-text{left:81px;top:1104px;width:810px;font-size:6.2px;line-height:8.2px;color:#2a2a2a}
.legal-text p+p{margin-top:8px}
</style>
</head>
<body>

<div class="abs brand"><span class="brand-mark"></span><span class="brand-name">HALVORSEN CAPITAL GROUP</span></div>

<nav class="abs nav">
  <a class="current">HOME</a>
  <a>ABOUT<span class="caret">&#8964;</span></a>
  <a>INVESTMENT<span class="caret">&#8964;</span></a>
  <a>FUNDS<span class="caret">&#8964;</span></a>
  <a>BROKERAGE<span class="caret">&#8964;</span></a>
  <a>EXCHANGE<span class="caret">&#8964;</span></a>
  <a>ACCOUNT<span class="caret">&#8964;</span></a>
  <a>CONTACT</a>
</nav>

<div class="abs hero-photo" role="img" aria-label="Black and white photo of five business people standing as a team"></div>
<div class="abs hero-title">TEAMWORK</div>
<div class="abs hero-sub">FOR YOUR BENIFIT</div>
<p class="abs hero-copy">Ut enim ad minim veniam, quis nostrud exercitation ullamcode laboris nisi dolore massa. Etaliquipx eato commodo conse cupiditate non</p>
<div class="abs hero-arrow" style="left:124px"><svg width="19" height="19"><path d="M11 5l-4 4.5 4 4.5" stroke="#fff" stroke-width="2" fill="none"/></svg></div>
<div class="abs hero-arrow" style="left:152px"><svg width="19" height="19"><path d="M8 5l4 4.5-4 4.5" stroke="#fff" stroke-width="2" fill="none"/></svg></div>

<section class="abs offer"></section>
<h2 class="abs offer-title">WHAT WE OFFER</h2>
<div class="abs sep" style="left:278px"></div>
<div class="abs sep" style="left:485px"></div>
<div class="abs sep" style="left:692px"></div>
<div class="abs card" style="left:298px">
  <div class="kicker">MANAGMENT</div><h3>STRATEGY</h3>
  <p>Ut enim ad minim veniam, quis nostrud exercitation ullamcode laboris nisi dolore massa Etaliquipx eato commodo conse cupiditate non</p>
  <span class="btn">MORE</span>
</div>
<div class="abs card" style="left:511px">
  <div class="kicker">FINANCIAL</div><h3>PLANNING</h3>
  <p>Ut enim ad minim veniam, quis nostrud exercitation ullamcode laboris nisi dolore massa Etaliquipx eato commodo conse cupiditate non</p>
  <span class="btn">MORE</span>
</div>
<div class="abs card" style="left:719px">
  <div class="kicker">CURRENCY</div><h3>EXCHANGE</h3>
  <p>Ut enim ad minim veniam, quis nostrud exercitation ullamcode laboris nisi dolore massa Etaliquipx eato commodo conse cupiditate non</p>
  <span class="btn">MORE</span>
</div>

<section class="abs do"></section>
<h2 class="abs do-title">WHAT WE DO</h2>
<p class="abs do-copy">Contrary to popular belief, Lorem Ipsum is not simply random text. It has roots in a piece of classical Latin literature from 45 BC, making it over 2000 years old. Elias Marrow, a Latin professor at Westbrook College in Virginia, looked up one of the more obscure Latin words, consectetur, from a Lorem Ipsum passage, and going through the cites of the word in classical literature, discovered the undoubtable source. Lorem Ipsum comes from sections 1.10.32 and 1.10.33 of "de Finibus Bonorum et Malorum" (The Extremes of Good and Evil) by Aurelian, written in 45 BC. This book is a treatise on the theory of ethics, very popular during the Renaissance. The first line of Lorem Ipsum, "Lorem ipsum dolor sit amet..",</p>
<div class="abs do-more">MORE &#187;</div>
<div class="abs rates">
  <span class="label">conversion</span>
  <span class="pair">GBP/EUR = <span class="down">1.18379 &#9660;</span></span>
  <span class="pair">GBP/AUD = <span class="down">1.69576 &#9660;</span></span>
  <span class="pair">GBP/CAD = <span class="down">1.62787 &#9660;</span></span>
  <span class="pair">GBP/USD = <span class="up">1.56967 &#9650;</span></span>
  <span class="pair">GBP/NZD = <span class="down">1.95511 &#9660;</span></span>
</div>

<div class="abs login">
  <span class="forgot">forgot pass ?</span>
  <svg class="key" width="34" height="32" viewBox="0 0 34 32"><circle cx="10" cy="10" r="7" fill="none" stroke="#888" stroke-width="3"/><path d="M15 15l13 13M23 23l3-3M26 26l3-3" stroke="#888" stroke-width="3"/></svg>
  <div class="head">LOGIN</div>
  <label style="top:58px">USER NAME</label>
  <div class="field" style="top:68px">username</div>
  <label style="top:100px">PASSWORD</label>
  <div class="field" style="top:111px">&#8226;&#8226;&#8226;&#8226;&#8226;&#8226;&#8226;&#8226;&#8226;&#8226;&#8226;&#8226;&#8226;&#8226;&#8226;&#8226;&#8226;&#8226;&#8226;&#8226;</div>
  <div class="remember"><svg width="9" height="8"><path d="M1 4l3 3 4-6" stroke="#3a9a3a" stroke-width="2" fill="none"/></svg>Remember me</div>
  <div class="bar">
    <div class="links"><b>Learn More</b> information<br><b>Registrate</b> free account</div>
    <div class="go">LOGIN</div>
  </div>
</div>

<div class="abs rule"></div>
<div class="abs trust-label">Verified and Protected by</div>
<svg class="abs badge" style="left:341px" width="76" height="36"><rect x="1" y="4" width="74" height="28" rx="14" fill="none" stroke="#9b1b2a" stroke-width="2"/></svg>
<svg class="abs badge" style="left:486px" width="80" height="36"><rect x="0" y="2" width="79" height="30" fill="#1f4a9a"/></svg>
<svg class="abs badge" style="left:634px" width="110" height="36"><rect x="0" y="3" width="30" height="30" fill="#6fb43f"/><rect x="36" y="11" width="70" height="14" fill="#8ac466" opacity=".5"/></svg>
<svg class="abs badge" style="left:800px" width="40" height="40"><circle cx="20" cy="18" r="18" fill="#1f3f7a" stroke="#e56a1f" stroke-width="2"/></svg>

<footer class="abs footer"></footer>
<div class="abs fcol" style="left:80px"><h4>ABOUT US</h4>History<br>Exprtize<br>Identity<br>Strategy<br>Contact us<br>Disclaimer</div>
<div class="abs fcol" style="left:151px"><h4>INVESTMENT</h4>Term Deposity<br>Managment and Strategy<br>Client Relations<br>Financial Privacy<br>Tax Advice<br>Wealth Analysis &amp; Finacial Planning<br>Active Advisory Group<br>Manager Selection services<br>Private Equity</div>
<div class="abs fcol" style="left:285px"><h4>FUNDS</h4>Overviewe<br>Administration<br>Funds Security<br>Core Services<br>Reporting<br>Revenue Oportunities<br>How it works?<br>Glossary</div>
<div class="abs fcol" style="left:383px"><h4>EXCHANGE</h4>Foreign Exchange<br>Fx Forword<br>Fx Options</div>
<div class="abs fcol" style="left:383px;top:1022px"><h4>ACCOUNTS</h4>Apply Now<br>Private Access</div>
<div class="abs fcol" style="left:471px;top:954px"><h4>BROKERAGE</h4>Institutional<br>Research<br>Trading</div>
<div class="abs social"><i></i><i></i><i></i><i></i><i></i></div>
<div class="abs copy">Copyright &#169; 2009-13 <b>Halvorsen Capital Group</b></div>

<div class="abs legal"></div>
<div class="abs legal-text">
  <p>Contrary to popular belief, Lorem Ipsum is not simply random text. It has roots in a piece of classical Latin literature from 45 BC, making it over 2000 years old. Elias Marrow, a Latin professor at Westbrook College in Virginia, looked up one of the more obscure Latin words, consectetur, from a Lorem Ipsum passage, and going through the cites of the word in classical literature, discovered the undoubtable source. Lorem Ipsum comes from sections 1.10.32 and 1.10.33 of "de Finibus Bonorum et Malorum" (The Extremes of Good and Evil) by Aurelian, written in 45 BC. This book is a treatise on the theory of ethics, very popular during the Renaissance. The first line of Lorem Ipsum, "Lorem ipsum dolor sit amet..", comes from a line in section 1.10.32.</p>
  <p>The standard chunk of Lorem Ipsum used since the 1500s is reproduced below for those interested. Sections 1.10.32 and 1.10.33 from "de Finibus Bonorum et Malorum" by Aurelian are also reproduced in their exact original form, accompanied by English versions from the 1914 translation by J. Thornfield. It is a long established fact that a reader will be distracted by the readable content of a page when looking at its layout. The point of using Lorem Ipsum is that it has a more-or-less normal distribution of letters, as opposed to using 'Content here, content here', making it look like readable English. Many desktop publishing packages and web page editors now use Lorem Ipsum as their default model text, and a search for 'lorem ipsum' will uncover many web sites still in their infancy. Various versions have evolved over the years, sometimes by accident, sometimes on purpose (injected humour and the like).</p>
</div>

</body>
</html>
```